Cybersecurity firm needs marketing template for professional services

Looking for a flyer design we can use as a template to market ten professional cybersecurity services (Pen Testing, V-CISO, SOC 2, KORVALD, etc). Each flyer will explain WHAT the service is, WHO needs it, DIFFERENT TYPES and SCOPE. Clean look/ lots of white space/ elevated graphics, Attached is a basic example but we are looking for something to WOW us.

```html
<!DOCTYPE html>
<html lang="en">
<head>
<meta charset="utf-8">
<title>Penetration Testing Flyer</title>
<link rel="stylesheet" href="https://fonts.googleapis.com/css2?family=Poppins:wght@500;600;700;800&family=Montserrat:wght@400;500;600&display=swap">
<style>
:root{
  --navy:#0d3566;
  --navy-deep:#0c2a4e;
  --blue:#0b77c5;
  --sky:#2ea9e0;
  --wave:#8ecbee;
  --dot:#bfe2f6;
  --orange:#f0a21c;
  --orange-deep:#ef7f1a;
  --slate:#3b4a5e;
  --steel:#6d86a6;
  --teal:#1d87bf;
  --ink:#1c2433;
  --grey:#8a93a0;
  --page:#e9edf1;
}
*{margin:0;padding:0;box-sizing:border-box}
html,body{width:1200px;height:2400px;overflow:hidden;background:var(--page)}
.flyer{position:absolute;left:0;top:351px;width:1200px;height:1697px;background:#fff;overflow:hidden;
  box-shadow:0 20px 50px rgba(0,0,0,.2);font-family:'Montserrat',sans-serif;color:var(--ink)}
.art{position:absolute;left:0;top:0;width:1200px;height:1697px}
.abs{position:absolute}
.brand-name{left:62px;top:188px;font-size:44px;font-weight:500;color:var(--navy);letter-spacing:-1px}
.brand-mark{left:64px;top:150px;width:22px;height:22px;border-radius:50%;background:var(--sky)}
.brand-tag{left:52px;top:246px;font-size:19px;color:var(--grey)}
.title-top{left:44px;top:288px;font-family:'Poppins',sans-serif;font-weight:700;font-size:74px;color:var(--blue);line-height:1}
.title-main{left:40px;top:360px;font-family:'Poppins',sans-serif;font-weight:800;font-size:118px;color:var(--navy);line-height:1;letter-spacing:-2px}
.series{left:48px;top:486px;font-family:'Poppins',sans-serif;font-weight:700;font-size:26px;letter-spacing:11px;color:var(--ink)}
.heading{font-family:'Poppins',sans-serif;font-weight:700;font-size:38px;color:var(--navy);line-height:1}
.heading span{color:var(--blue)}
.body{font-size:18px;line-height:22.5px;text-align:justify;color:var(--ink)}
.what-h{left:55px;top:555px}
.what-p{left:55px;top:605px;width:505px}
.who-h{left:55px;top:805px}
.who-p{left:55px;top:856px;width:517px}
.tools-h{left:59px;top:1058px}
.divider{left:590px;top:565px;width:2px;height:240px;background:#d5dbe2}
.tech-h{left:623px;top:609px}
.tech-p{left:623px;top:659px;width:516px;font-size:19.5px;line-height:24px}
.tools{top:1112px;list-style:none;font-size:18px;line-height:24.4px;white-space:nowrap}
.tools li b{display:inline-block;width:28px;font-weight:600;font-size:13px;color:var(--blue)}
.col1{left:53px}.col2{left:245px}.col3{left:412px}
.band{left:0;top:1441px;width:1200px;height:256px;background:var(--navy-deep)}
.cta{left:85px;top:1409px;width:1035px;height:68px;border-radius:34px;background:var(--sky);color:#fff;
  font-family:'Poppins',sans-serif;font-weight:700;font-size:46px;letter-spacing:12px;text-align:center;line-height:70px}
.contact-h{left:0;top:1495px;width:1200px;text-align:center;color:#fff;font-family:'Poppins',sans-serif;font-weight:600;font-size:30px;letter-spacing:7px}
.info{color:#fff;font-family:'Poppins',sans-serif;font-weight:600;font-size:23px;line-height:32px}
.addr{left:95px;top:1540px}
.phone{left:95px;top:1618px}
.mail{left:705px;top:1556px}
.web{left:705px;top:1595px;font-size:38px;line-height:50px;letter-spacing:1px}
.web span{color:var(--sky)}
</style>
</head>
<body>
<div class="flyer">
  <svg class="art" viewBox="0 0 1200 1697">
    <defs>
      <linearGradient id="seaTone" x1="0" y1="0" x2="1" y2="1">
        <stop offset="0" stop-color="#2a6ea6"/>
        <stop offset="1" stop-color="#0e3f73"/>
      </linearGradient>
      <clipPath id="innerDisc"><circle cx="881" cy="1060" r="168"/></clipPath>
      <filter id="soft" x="-30%" y="-30%" width="160%" height="160%">
        <feDropShadow dx="0" dy="6" stdDeviation="7" flood-color="#0d3566" flood-opacity=".22"/>
      </filter>
    </defs>
    <path d="M300 0 C400 0 480 180 560 330 C660 520 900 580 1200 565 L1200 0 Z" fill="var(--wave)"/>
    <path d="M330 0 C425 0 505 140 585 285 C675 440 860 480 1200 445 L1200 0 Z" fill="url(#seaTone)" role="img" aria-label="Photograph of a great white shark swimming in deep blue water"/>

    <g fill="var(--dot)">
      <circle cx="1110" cy="1148" r="15"/><circle cx="1168" cy="1232" r="23"/>
      <circle cx="1190" cy="1290" r="24"/><circle cx="1137" cy="1336" r="36"/>
      <circle cx="1059" cy="1323" r="20"/><circle cx="1000" cy="1380" r="44"/>
      <circle cx="1160" cy="1410" r="38"/><circle cx="1090" cy="1202" r="10"/>
    </g>

    <circle cx="881" cy="1060" r="186" fill="none" stroke="var(--dot)" stroke-width="26"/>
    <g filter="url(#soft)" fill="#fff">
      <circle cx="782" cy="899" r="84"/><circle cx="966" cy="899" r="84"/>
      <circle cx="695" cy="1058" r="84"/><circle cx="1053" cy="1060" r="84"/>
      <circle cx="782" cy="1215" r="84"/><circle cx="966" cy="1215" r="84"/>
    </g>
    <g clip-path="url(#innerDisc)">
      <circle cx="782" cy="899" r="84" fill="var(--orange)"/>
      <circle cx="966" cy="899" r="84" fill="var(--orange-deep)"/>
      <circle cx="695" cy="1058" r="84" fill="var(--slate)"/>
      <circle cx="1053" cy="1060" r="84" fill="var(--teal)"/>
      <circle cx="782" cy="1215" r="84" fill="var(--steel)"/>
      <circle cx="966" cy="1215" r="84" fill="var(--navy)"/>
    </g>
    <circle cx="881" cy="1060" r="103" fill="#fff"/>

    <g fill="none" stroke="#fff" stroke-width="3" stroke-linecap="round">
      <circle cx="812" cy="940" r="12"/><line x1="821" y1="949" x2="834" y2="962"/>
      <rect x="924" y="924" width="26" height="32" rx="3"/><line x1="944" y1="952" x2="962" y2="934"/>
      <circle cx="731" cy="1058" r="13"/><line x1="731" y1="1038" x2="731" y2="1078"/><line x1="711" y1="1058" x2="751" y2="1058"/>
      <rect x="1003" y="1042" width="30" height="36" rx="3"/><polyline points="1009,1070 1016,1062 1022,1067 1028,1058"/>
      <rect x="800" y="1172" width="34" height="24" rx="3"/><line x1="808" y1="1178" x2="808" y2="1190"/><line x1="816" y1="1178" x2="816" y2="1190"/><line x1="824" y1="1178" x2="824" y2="1190"/>
      <line x1="934" y1="1172" x2="960" y2="1172"/><line x1="934" y1="1182" x2="960" y2="1182"/><line x1="934" y1="1192" x2="960" y2="1192"/>
    </g>

    <g font-family="Poppins, sans-serif" font-weight="600" font-size="21" fill="var(--ink)">
      <text x="772" y="885" text-anchor="middle">Research</text>
      <text x="984" y="885" text-anchor="middle">Cleanup</text>
      <text x="654" y="1064" text-anchor="middle">Scope</text>
      <text x="1087" y="1050" text-anchor="middle">Report</text>
      <text x="1087" y="1075" text-anchor="middle">Writing</text>
      <text x="772" y="1244" text-anchor="middle">Scanning</text>
      <text x="966" y="1244" text-anchor="middle">Enumeration</text>
    </g>
    <g font-family="Poppins, sans-serif" font-weight="700" font-size="32" fill="var(--blue)" text-anchor="middle">
      <text x="881" y="1053">PEN TEST</text>
      <text x="881" y="1086">CYCLE</text>
    </g>
  </svg>

  <div class="abs brand-mark"></div>
  <div class="abs brand-name">tidewellgroup</div>
  <div class="abs brand-tag">Cybersecurity | Risk | Audit | Advisory</div>

  <h1 class="abs title-top">PENETRATION</h1>
  <div class="abs title-main">TESTING</div>
  <div class="abs series">TIDEWELL INSIGHTS SERIES</div>

  <h2 class="abs heading what-h">What <span>It Is?</span></h2>
  <p class="abs body what-p">A mature penetration test is an in-depth security assessment where ethical hackers attempt to exploit system vulnerabilities to gain access to sensitive data or systems. It is an important security practice because it can help organizations identify vulnerabilities that attackers may exploit in order to gain access to confidential information, disrupt services, or even cause physical damage to the network or system.</p>

  <div class="abs divider"></div>

  <h2 class="abs heading who-h">Who <span>needs It?</span></h2>
  <p class="abs body who-p">A mature penetration test is an in-depth security assessment where ethical hackers attempt to exploit system vulnerabilities to gain access to sensitive data or systems. It is an important security practice because it can help organizations identify vulnerabilities that attackers may exploit in order to gain access to confidential information, disrupt services, or even cause physical damage to the network or system.</p>

  <h2 class="abs heading tools-h">Testing <span>Tools</span></h2>
  <ul class="abs tools col1">
    <li><b>1.</b>Portvane</li><li><b>2.</b>Brisklet Suite</li><li><b>3.</b>Exploravel</li><li><b>4.</b>Wirequill</li>
    <li><b>5.</b>Hashmorrow</li><li><b>6.</b>Scandrel</li><li><b>7.</b>Sitevarn</li><li><b>8.</b>Querrow</li>
    <li><b>9.</b>Vulnarch</li><li><b>10.</b>Loginvise</li><li><b>11.</b>Airglint</li>
  </ul>
  <ul class="abs tools col2">
    <li><b>12.</b>Wavemire</li><li><b>13.</b>Credwick</li><li><b>14.</b>Tunnelvane</li><li><b>15.</b>Hostmere</li>
    <li><b>16.</b>Dirquell</li><li><b>17.</b>Netbrindle</li><li><b>18.</b>Namequill</li><li><b>19.</b>Midtrap</li>
    <li><b>20.</b>Bannerwisp</li><li><b>21.</b>Pingmoor</li><li><b>22.</b>Openvarn</li>
  </ul>
  <ul class="abs tools col3" style="top:1110px">
    <li><b>23.</b>Lurevane</li><li><b>24.</b>Portvane Scripts</li><li><b>25.</b>Engine</li><li><b>26.</b>Coremarrow</li>
    <li><b>27.</b>Linkfennel</li><li><b>28.</b>Metaquill</li><li><b>29.</b>Webtallow</li><li><b>30.</b>Skiffnet</li>
    <li><b>31.</b>Proxwarden</li>
  </ul>

  <h2 class="abs heading tech-h">Testing <span>Techniques</span></h2>
  <p class="abs body tech-p">A wide range of techniques are used to identify security weaknesses, such as vulnerability scanning, application security testing, manual testing, and web application testing.</p>

  <div class="abs band"></div>
  <div class="abs cta">CONSIDERING A PEN TEST?</div>
  <div class="abs contact-h">CONTACT OUR EXPERT</div>

  <svg class="abs" style="left:54px;top:1545px" width="28" height="34" viewBox="0 0 28 34"><path d="M14 0C6 0 0 6 0 14c0 10 14 20 14 20s14-10 14-20C28 6 22 0 14 0z" fill="var(--sky)"/><circle cx="14" cy="13" r="5" fill="var(--navy-deep)"/></svg>
  <div class="abs info addr">2210 N. Harbor Lane, Suite 410<br>Westfield, OH 43190</div>
  <svg class="abs" style="left:54px;top:1624px" width="30" height="20" viewBox="0 0 30 20"><rect width="30" height="20" rx="2" fill="var(--sky)"/><polyline points="1,2 15,12 29,2" fill="none" stroke="var(--navy-deep)" stroke-width="2.5"/></svg>
  <div class="abs info phone">800-555-0147</div>

  <svg class="abs" style="left:664px;top:1560px" width="28" height="28" viewBox="0 0 24 24"><path d="M6.6 10.8a15 15 0 006.6 6.6l2.2-2.2a1 1 0 011-.25 11.4 11.4 0 003.6.57 1 1 0 011 1V20a1 1 0 01-1 1A17 17 0 013 4a1 1 0 011-1h3.5a1 1 0 011 1c0 1.25.2 2.45.57 3.57a1 1 0 01-.25 1z" fill="#fff"/></svg>
  <div class="abs info mail">pentest@tidewellpro.com</div>
  <svg class="abs" style="left:664px;top:1610px" width="28" height="28" viewBox="0 0 28 28"><circle cx="14" cy="14" r="12" fill="none" stroke="var(--sky)" stroke-width="3"/><ellipse cx="14" cy="14" rx="5" ry="12" fill="none" stroke="var(--sky)" stroke-width="2.5"/><line x1="2" y1="14" x2="26" y2="14" stroke="var(--sky)" stroke-width="2.5"/></svg>
  <div class="abs info web">www.<span>tidewellpro</span>.com</div>
</div>
</body>
</html>
```